Physician and Alternative Investments Investor needs a business card design.

I am making a career change from a plastic surgeon to a career as an investor. I am primarily involved with Angel Investing. I really want a fairly simple design overall and don't need to list angel investing unless it can be done very subtly, perhaps via an image rather than verbiage. A design without any mention of angel investing is completely acceptable. My credentials are "MD, MBA." I will also want to place my email address and mobile phone number and have provided below.

Target Market(s)

business contacts (physicians and non-physicians in the business world)

Industry/Entity Type

Business

Requirements
Must have
• Colin Pettigrew
• MD, MBA
• drcolinpettigrew@mailvane.net
• cell 770.548.2913
Should not have
• Clutter.

```html
<!DOCTYPE html>
<html lang="en">
<head>
<meta charset="utf-8">
<title>Colin Pettigrew — Business Card</title>
<link rel="stylesheet" href="https://fonts.googleapis.com/css2?family=Open+Sans:wght@400;600;700&family=Questrial&display=swap">
<style>
  :root {
    --backdrop: #2b2b2d;
    --card: #1c1c1e;
    --card-edge: #262628;
    --brand-blue: #1c4f9e;
    --name-grey: #a3a3a6;
    --detail-white: #e6e6e8;
    --icon-fill: #1c4f9e;
    --icon-glyph: #ffffff;
  }
  * { box-sizing: border-box; margin: 0; padding: 0; }
  html, body {
    width: 1200px; height: 900px; overflow: hidden;
    background: var(--backdrop);
  }
  .canvas {
    width: 1200px; height: 900px;
    display: flex; align-items: center; justify-content: center; gap: 60px;
  }
  .card {
    position: relative;
    width: 520px; height: 300px;
    background: var(--card);
    border: 1px solid var(--card-edge);
    border-radius: 22px;
    box-shadow: 0 18px 40px rgba(0,0,0,.45);
  }

  /* Front: details side */
  .card-front .brand-mark {
    position: absolute; left: 44px; top: 118px;
    font-family: "Open Sans", sans-serif; font-weight: 600;
    font-size: 24px; color: var(--brand-blue); letter-spacing: .2px;
  }
  .card-front .identity {
    position: absolute; right: 40px; top: 96px; text-align: right;
    font-family: "Open Sans", sans-serif; color: var(--name-grey);
  }
  .identity .person-name { font-size: 15px; font-weight: 700; line-height: 1.15; }
  .identity .credentials { font-size: 12px; font-weight: 600; }
  .contact-list {
    position: absolute; right: 40px; top: 176px; list-style: none;
    font-family: "Open Sans", sans-serif; font-size: 13px; color: var(--detail-white);
    text-align: right;
  }
  .contact-list li { display: flex; align-items: center; justify-content: flex-end; gap: 7px; height: 22px; }
  .contact-list .phone { padding-right: 0; }
  .contact-list .email { margin-right: 0; }
  .contact-icon { width: 14px; height: 14px; flex: none; }

  /* Back: brand side */
  .card-back .brand-mark {
    position: absolute; left: 0; right: 0; top: 58px; text-align: center;
    font-family: "Open Sans", sans-serif; font-weight: 600;
    font-size: 22px; color: var(--brand-blue);
  }
  .card-back .signature {
    position: absolute; left: 0; right: 0; top: 150px; text-align: center;
    font-family: "Questrial", sans-serif; color: var(--brand-blue);
  }
  .signature .person-name { font-size: 38px; letter-spacing: 1px; line-height: 1; }
  .signature .credentials {
    display: block; font-size: 15px; letter-spacing: 1px;
    text-align: right; width: 392px; margin: 6px auto 0;
  }
</style>
</head>
<body>
<main class="canvas">
  <section class="card card-front" aria-label="Card front">
    <div class="brand-mark">Colin Pettigrew</div>
    <div class="identity">
      <div class="person-name">Colin Pettigrew</div>
      <div class="credentials">MD, MBA</div>
    </div>
    <ul class="contact-list">
      <li class="phone">770.548.2913
        <svg class="contact-icon" viewBox="0 0 14 14" aria-hidden="true">
          <rect width="14" height="14" rx="2" fill="var(--icon-fill)"/>
          <path d="M4.2 3.2c.4-.3.9-.2 1.1.2l.7 1.3c.2.4.1.8-.2 1l-.5.4c.4.9 1.1 1.6 2 2l.4-.5c.3-.3.7-.4 1-.2l1.3.7c.4.2.5.7.2 1.1l-.5.6c-.5.5-1.3.6-2 .3C5.9 9.3 4.7 8.1 4 6.3c-.3-.7-.2-1.5.3-2z" fill="var(--icon-glyph)"/>
        </svg>
      </li>
      <li class="email">drcolinpettigrew@mailvane.net
        <svg class="contact-icon" viewBox="0 0 14 14" aria-hidden="true">
          <rect width="14" height="14" rx="2" fill="var(--icon-fill)"/>
          <rect x="3" y="4.5" width="8" height="5.5" rx=".6" fill="var(--icon-glyph)"/>
          <path d="M3.2 4.8L7 7.6l3.8-2.8" fill="none" stroke="var(--icon-fill)" stroke-width=".8"/>
        </svg>
      </li>
    </ul>
  </section>

  <section class="card card-back" aria-label="Card back">
    <div class="brand-mark">Colin Pettigrew</div>
    <div class="signature">
      <div class="person-name">Colin Pettigrew</div>
      <span class="credentials">MD, MBA</span>
    </div>
  </section>
</main>
</body>
</html>
```